The Christian Teacher Life-Cycle

Look at the Lifecyle of the Christian School.
Look at the BLT logo.
I am looking for a Christian Teacher Lifecycle that represents the slides in the PP upload.
Our website is bramblewoodlearningtrust.org.
The design should include a summary design showing all four stages, and then four slides representing each of the stages as subsets of the summary design.
When a teacher is going through the Lifecycle, they are going on their Professional Learning Journey that takes 40 years to unfold.
All five should include a copyright 2026 BLT on them.

```html
<!DOCTYPE html>
<html lang="en">
<head>
<meta charset="utf-8">
<title>Christian Teacher Lifecycle – BLT</title>
<link href="https://fonts.googleapis.com/css2?family=Montserrat:wght@400;500;600;700;800&display=swap" rel="stylesheet">
<style>
:root{
  --navy:#14285a;
  --navy-deep:#0f1f4a;
  --green:#2f6b2a;
  --green-bright:#6fbf3a;
  --blue:#1e4fa8;
  --ink:#2a2f3a;
  --grey:#5a6070;
  --paper:#ffffff;
  --canvas:#eef0f3;
}
*{box-sizing:border-box;margin:0;padding:0}
html,body{width:1200px;height:800px;overflow:hidden;background:var(--canvas);font-family:'Montserrat',sans-serif;color:var(--ink)}
.slide{position:absolute;overflow:hidden;background:var(--paper)}
.slide-summary{left:8px;top:8px;width:738px;height:430px}
.slide-s1{left:760px;top:8px;width:432px;height:430px}
.slide-s2{left:8px;top:448px;width:384px;height:344px}
.slide-s3{left:403px;top:448px;width:357px;height:344px}
.slide-s4{left:772px;top:448px;width:420px;height:344px}

.scene{position:absolute}
.page-tag{position:absolute;top:0;right:0;background:var(--navy-deep);color:#fff;font-size:11px;font-weight:700;padding:6px 12px;letter-spacing:.5px}
.brand{position:absolute;display:flex;align-items:center;gap:8px}
.brand-name{font-weight:600;color:var(--navy);letter-spacing:1px}
.brand-dot{width:14px;height:14px;border-radius:50%;background:var(--green)}
.copyright{position:absolute;font-size:9px;color:var(--ink);font-weight:500}

/* summary */
.summary-title{position:absolute;left:30px;top:80px}
.summary-title .t1{font-size:24px;font-weight:800;color:var(--navy);letter-spacing:.3px;line-height:1.1}
.summary-title .t2{font-size:46px;font-weight:800;color:var(--green);line-height:1;letter-spacing:1px}
.summary-title .t3{font-size:11.5px;font-weight:600;color:var(--grey);letter-spacing:1.6px;margin-top:5px}
.summary-intro{position:absolute;left:30px;top:192px;width:122px;font-size:9.5px;line-height:1.6}
.summary-head{position:absolute;left:354px;top:44px;width:200px;text-align:center;font-size:12px;font-weight:700;color:var(--navy);line-height:1.35}
.summary-head .accent{color:var(--green)}
.summary-head .rule{width:70px;height:1px;background:var(--navy);margin:7px auto 0}
.journey{position:absolute;left:0;top:0}
.stage-label{position:absolute;width:120px;text-align:center}
.stage-label .num{font-size:11px;font-weight:700}
.stage-label .name{font-size:9px;font-weight:700;color:var(--navy);line-height:1.3}
.stage-label .yrs{font-size:9.5px;font-weight:700;color:var(--navy);margin:6px 0 4px}
.stage-label .desc{font-size:7.2px;line-height:1.6;color:var(--ink)}
.summary-band{position:absolute;left:0;bottom:0;width:100%;height:32px;background:var(--navy-deep);display:flex;align-items:center;padding-left:20px;color:#fff;font-size:8.5px;font-weight:600;letter-spacing:.8px;line-height:1.3}
.summary-band .line{width:58px;height:1px;background:var(--green-bright);margin-right:14px}
.summary-band .hi{color:var(--green-bright)}
.summary-band .copy{position:absolute;right:14px;font-weight:500;letter-spacing:0}

/* stage slides */
.stage-head{position:absolute}
.stage-head .st{font-size:24px;font-weight:800;line-height:1}
.stage-head .sn{font-size:13.5px;font-weight:700;line-height:1.3;margin-top:6px}
.stage-head .rule{width:26px;height:1.5px;margin:12px 0 14px}
.stage-head .yrs{font-size:12px;font-weight:700}
.stage-head .lede{font-size:9px;line-height:1.55;margin-top:18px;width:118px}
.tone-navy{color:var(--navy)} .tone-navy .rule{background:var(--navy)}
.tone-green{color:var(--green)} .tone-green .rule{background:var(--green)}
.tone-blue{color:var(--blue)} .tone-blue .rule{background:var(--blue)}
.stage-head .lede{color:var(--ink)}
.points{position:absolute;list-style:none}
.point{display:flex;align-items:flex-start;gap:10px}
.icon{flex:none;width:32px;height:32px;border-radius:50%;display:flex;align-items:center;justify-content:center}
.icon-solid-navy{background:var(--navy)}
.icon-solid-green{background:var(--green)}
.icon-ring-blue{border:1.5px solid var(--blue);background:#fff}
.icon-ring-green{border:1.5px solid var(--green);background:#fff}
.point h4{font-size:8.5px;font-weight:700;margin-top:3px}
.point p{font-size:7.5px;line-height:1.6;color:var(--ink)}
</style>
</head>
<body>

<!-- Summary -->
<section class="slide slide-summary">
  <div class="scene" role="img" aria-label="Misty mountain landscape with a winding path climbing to a summit cross in sunrise light" style="left:300px;top:0;width:438px;height:398px;background:linear-gradient(100deg,rgba(255,255,255,1) 0%,rgba(236,240,242,.9) 22%,#c9d3da 45%,#8e9aa3 65%,#6f7f6a 85%,#56704a 100%)"></div>
  <div class="page-tag">1 OF 5</div>
  <div class="brand" style="left:30px;top:28px">
    <span class="brand-dot"></span><span class="brand-name" style="font-size:26px">BLT</span>
  </div>
  <div class="summary-title">
    <div class="t1">CHRISTIAN TEACHER</div>
    <div class="t2">LIFECYCLE</div>
    <div class="t3">PROFESSIONAL LEARNING JOURNEY</div>
  </div>
  <p class="summary-intro">A 40-year journey of growth, leadership, and legacy that transforms lives for Christ and for generations to come.</p>
  <div class="summary-head"><span class="accent">A 40-YEAR JOURNEY</span><br>OF CALLING, GROWTH,<br>LEADERSHIP, AND LEGACY<div class="rule"></div></div>

  <svg class="journey" width="738" height="398" viewBox="0 0 738 398">
    <path d="M85 315 C120 290 140 275 165 265 C210 250 230 245 260 225 C300 195 330 200 360 200 C400 198 400 175 420 170 C460 160 470 172 510 165 C540 160 560 150 590 148" fill="none" stroke="var(--navy)" stroke-width="9" stroke-linecap="round" opacity=".9"/>
    <g fill="#fff" stroke="var(--navy)" stroke-width="1.5"><circle cx="233" cy="240" r="3"/><circle cx="352" cy="201" r="3"/><circle cx="482" cy="166" r="3"/></g>
    <g>
      <path d="M176 282 l-8 -10 h16z" fill="var(--navy)"/><circle cx="176" cy="252" r="28" fill="var(--navy)"/><circle cx="176" cy="252" r="22" fill="#fff"/>
      <path d="M176 262 v-12 M176 252 c-6 -8 -12 -4 -12 -4 c4 6 12 4 12 4 M176 250 c6 -8 12 -4 12 -4 c-4 6 -12 4 -12 4" stroke="var(--navy)" stroke-width="2" fill="none"/>
    </g>
    <g>
      <path d="M290 238 l-8 -10 h16z" fill="var(--green)"/><circle cx="290" cy="208" r="28" fill="var(--green)"/><circle cx="290" cy="208" r="22" fill="#fff"/>
      <path d="M290 220 v-18 M290 212 c-7 -3 -8 -9 -8 -9 c6 1 8 6 8 9 M290 208 c7 -3 8 -9 8 -9 c-6 1 -8 6 -8 9" stroke="var(--green)" stroke-width="2" fill="none"/>
      <circle cx="290" cy="250" r="10" fill="var(--green)"/><text x="290" y="254" font-size="11" font-weight="700" fill="#fff" text-anchor="middle" font-family="Montserrat,sans-serif">2</text>
    </g>
    <g>
      <path d="M415 195 l-8 -10 h16z" fill="var(--blue)"/><circle cx="415" cy="165" r="28" fill="var(--blue)"/><circle cx="415" cy="165" r="22" fill="#fff"/>
      <g fill="var(--blue)"><circle cx="408" cy="160" r="3.5"/><circle cx="415" cy="158" r="4"/><circle cx="422" cy="160" r="3.5"/><path d="M402 173 q6 -10 13 -10 q7 0 13 10z"/></g>
      <circle cx="415" cy="213" r="10" fill="var(--blue)"/><text x="415" y="217" font-size="11" font-weight="700" fill="#fff" text-anchor="middle" font-family="Montserrat,sans-serif">3</text>
    </g>
    <g transform="translate(0,12)">
      <path d="M553 152 l-8 -10 h16z" fill="var(--green)"/><circle cx="553" cy="122" r="28" fill="var(--green)"/><circle cx="553" cy="122" r="22" fill="#fff"/>
      <circle cx="553" cy="116" r="9" fill="none" stroke="var(--green)" stroke-width="2"/><path d="M553 125 v10 M547 135 h12" stroke="var(--green)" stroke-width="2"/>
      <circle cx="553" cy="173" r="10" fill="var(--green)"/><text x="553" y="177" font-size="11" font-weight="700" fill="#fff" text-anchor="middle" font-family="Montserrat,sans-serif">4</text>
    </g>
  </svg>

  <div class="stage-label" style="left:116px;top:290px"><div class="num tone-navy">STAGE 1</div><div class="name">CALLING &amp;<br>FOUNDATION</div><div class="yrs">YEARS 1–10</div><div class="desc">Discovering God's call and building a strong spiritual and professional foundation.</div></div>
  <div class="stage-label" style="left:230px;top:266px"><div class="num tone-green">STAGE 2</div><div class="name">GROWTH &amp;<br>DEVELOPMENT</div><div class="yrs">YEARS 11–20</div><div class="desc">Growing in expertise, character, and impact through continuous learning and service.</div></div>
  <div class="stage-label" style="left:355px;top:229px"><div class="num tone-blue">STAGE 3</div><div class="name">LEADERSHIP &amp;<br>INFLUENCE</div><div class="yrs">YEARS 21–30</div><div class="desc">Leading others, expanding influence, and shaping the next generation of educators.</div></div>
  <div class="stage-label" style="left:493px;top:204px"><div class="num tone-green">STAGE 4</div><div class="name">LEGACY &amp;<br>MULTIPLICATION</div><div class="yrs">YEARS 31–40</div><div class="desc">Mentoring and multiplying leaders to leave a lasting Kingdom impact.</div></div>

  <div class="summary-band"><span class="line"></span><span>EQUIPPING AND EMPOWERING CHRISTIAN EDUCATORS<br>FOR A LIFETIME OF <span class="hi">KINGDOM IMPACT</span></span><span class="copy">© 2026 BLT</span></div>
</section>

<!-- Stage 1 -->
<section class="slide slide-s1">
  <div class="scene" role="img" aria-label="Young green seedling growing from soil in soft morning light" style="left:150px;top:0;width:282px;height:430px;background:linear-gradient(90deg,#fff 0%,#eef1ec 30%,#c9d4bb 60%,#8aa060 80%,#4c4a3a 100%)"></div>
  <div class="page-tag">2 OF 5</div>
  <div class="stage-head tone-navy" style="left:26px;top:34px">
    <div class="st">STAGE 1</div><div class="sn">CALLING &amp;<br>FOUNDATION</div><div class="rule"></div><div class="yrs">YEARS 1–10</div>
  </div>
  <ul class="points" style="left:24px;top:160px">
    <li class="point" style="margin-bottom:14px"><span class="icon icon-solid-navy"><svg width="14" height="14" viewBox="0 0 14 14"><rect x="2" y="1" width="10" height="12" fill="#fff"/><path d="M7 3v6M5 5h4" stroke="var(--navy)" stroke-width="1.3"/></svg></span><div><h4 class="tone-navy">Deepen Faith</h4><p>Grow in Christ and His Word</p></div></li>
    <li class="point" style="margin-bottom:14px"><span class="icon icon-solid-navy"><svg width="16" height="16" viewBox="0 0 16 16"><circle cx="8" cy="8" r="6" fill="none" stroke="#fff" stroke-width="1.4"/><path d="M11 5 L9 9 L5 11 L7 7z" fill="#fff"/></svg></span><div><h4 class="tone-navy">Build Foundation</h4><p>Develop core skills and confidence</p></div></li>
    <li class="point" style="margin-bottom:14px"><span class="icon icon-solid-navy"><svg width="16" height="16" viewBox="0 0 16 16"><circle cx="8" cy="6" r="3" fill="#fff"/><path d="M3 14q5 -7 10 0z" fill="#fff"/></svg></span><div><h4 class="tone-navy">Early Impact</h4><p>Make a difference in the classroom</p></div></li>
    <li class="point"><span class="icon icon-solid-navy"><svg width="16" height="16" viewBox="0 0 16 16"><path d="M2 10h4l3 2h5v2H2z" fill="#fff"/><circle cx="10" cy="5" r="2.5" fill="#fff"/></svg></span><div><h4 class="tone-navy">Seek Guidance</h4><p>Learn from mentors</p></div></li>
  </ul>
  <div class="brand" style="left:22px;top:388px"><span class="brand-dot"></span><span class="brand-name" style="font-size:18px">BLT</span></div>
  <div class="copyright" style="right:14px;top:412px">© 2026 BLT</div>
</section>

<!-- Stage 2 -->
<section class="slide slide-s2">
  <div class="scene" role="img" aria-label="Green forested hillside with a winding trail through misty mountains" style="left:0;top:0;width:384px;height:344px;background:linear-gradient(180deg,#fff 0%,#fff 45%,#dde6d6 58%,#9fb984 72%,#5f8a45 88%,#3f6a30 100%)"></div>
  <div class="page-tag">3 OF 5</div>
  <div class="stage-head tone-green" style="left:22px;top:30px">
    <div class="st">STAGE 2</div><div class="sn">GROWTH &amp;<br>DEVELOPMENT</div><div class="rule"></div><div class="yrs">YEARS 11–20</div>
    <p class="lede">Growing in expertise, character, and impact through continuous learning and service.</p>
  </div>
  <ul class="points" style="left:178px;top:34px">
    <li class="point" style="margin-bottom:12px"><span class="icon icon-solid-green"><svg width="16" height="14" viewBox="0 0 16 14"><path d="M1 2q4-1 7 1q3-2 7-1v10q-4-1-7 1q-3-2-7-1z" fill="none" stroke="#fff" stroke-width="1.4"/><path d="M8 3v10" stroke="#fff" stroke-width="1.2"/></svg></span><div><h4 class="tone-green">Expand Expertise</h4><p>Strengthen teaching<br>and subject knowledge</p></div></li>
    <li class="point" style="margin-bottom:12px"><span class="icon icon-solid-green"><svg width="16" height="16" viewBox="0 0 16 16"><path d="M3 14V10M7 14V8M11 14V6" stroke="#fff" stroke-width="2"/><path d="M2 8l5-4 3 2 4-4" stroke="#fff" stroke-width="1.3" fill="none"/></svg></span><div><h4 class="tone-green">Develop Character</h4><p>Grow in integrity,<br>humility, and resilience</p></div></li>
    <li class="point" style="margin-bottom:12px"><span class="icon icon-solid-green"><svg width="16" height="16" viewBox="0 0 16 16"><circle cx="5" cy="6" r="2.5" fill="#fff"/><circle cx="11" cy="6" r="2.5" fill="#fff"/><path d="M1 14q4-6 7 0M8 14q4-6 7 0" fill="#fff"/></svg></span><div><h4 class="tone-green">Increase Impact</h4><p>Take on greater<br>responsibility</p></div></li>
    <li class="point"><span class="icon icon-solid-green"><svg width="18" height="14" viewBox="0 0 18 14"><path d="M9 1l8 4-8 4-8-4z" fill="#fff"/><path d="M4 7v4q5 3 10 0V7" fill="#fff"/></svg></span><div><h4 class="tone-green">Lifelong Learning</h4><p>Pursue excellence<br>continually</p></div></li>
  </ul>
  <div class="brand" style="left:14px;top:314px"><span class="brand-dot" style="background:#fff"></span><span class="brand-name" style="font-size:18px;color:#fff">BLT</span></div>
  <div class="copyright" style="right:14px;top:322px;color:#fff">© 2026 BLT</div>
</section>

<!-- Stage 3 -->
<section class="slide slide-s3">
  <div class="scene" role="img" aria-label="Hikers on a rocky summit overlooking layered blue mountain ranges" style="left:0;top:0;width:357px;height:344px;background:linear-gradient(180deg,#fff 0%,#f3f5f8 40%,#cdd6e2 58%,#8a9ab0 75%,#4d5a6c 100%)"></div>
  <div class="page-tag">4 OF 5</div>
  <div class="stage-head tone-blue" style="left:25px;top:30px">
    <div class="st">STAGE 3</div><div class="sn">LEADERSHIP &amp;<br>INFLUENCE</div><div class="rule"></div><div class="yrs">YEARS 21–30</div>
    <p class="lede" style="width:110px">Leading others, expanding influence, and shaping the next generation of educators.</p>
  </div>
  <ul class="points" style="left:166px;top:34px">
    <li class="point" style="margin-bottom:11px"><span class="icon icon-ring-blue"><svg width="16" height="16" viewBox="0 0 16 16"><circle cx="5" cy="6" r="2.5" fill="var(--blue)"/><circle cx="11" cy="6" r="2.5" fill="var(--blue)"/><path d="M1 14q4-6 7 0M8 14q4-6 7 0" fill="var(--blue)"/></svg></span><div><h4 class="tone-blue">Lead Others</h4><p>Inspire and equip<br>fellow educators</p></div></li>
    <li class="point" style="margin-bottom:11px"><span class="icon icon-ring-blue"><svg width="16" height="16" viewBox="0 0 16 16"><circle cx="8" cy="8" r="5" fill="none" stroke="var(--blue)" stroke-width="3" stroke-dasharray="2.6 1.3"/><circle cx="8" cy="8" r="2" fill="var(--blue)"/></svg></span><div><h4 class="tone-blue">Build Systems</h4><p>Improve processes<br>and school culture</p></div></li>
    <li class="point" style="margin-bottom:11px"><span class="icon icon-ring-blue"><svg width="16" height="16" viewBox="0 0 16 16"><path d="M2 6h3l7-4v12l-7-4H2z" fill="var(--blue)"/></svg></span><div><h4 class="tone-blue">Expand Influence</h4><p>Serve beyond the<br>classroom</p></div></li>
    <li class="point"><span class="icon icon-ring-blue"><svg width="16" height="16" viewBox="0 0 16 16"><circle cx="8" cy="5" r="3" fill="var(--blue)"/><path d="M2 15q6-9 12 0z" fill="var(--blue)"/></svg></span><div><h4 class="tone-blue">Develop Leaders</h4><p>Mentor and raise up<br>future leaders</p></div></li>
  </ul>
  <div class="brand" style="left:16px;top:314px"><span class="brand-dot" style="background:#fff"></span><span class="brand-name" style="font-size:18px;color:#fff">BLT</span></div>
  <div class="copyright" style="right:14px;top:322px;color:#fff">© 2026 BLT</div>
</section>

<!-- Stage 4 -->
<section class="slide slide-s4">
  <div class="scene" role="img" aria-label="Family walking on a sunlit hilltop beneath a large tree at golden hour" style="left:0;top:0;width:420px;height:344px;background:linear-gradient(180deg,#fff 0%,#fbf7ee 40%,#efdfb6 58%,#c9a460 74%,#6f6a35 88%,#3e4424 100%)"></div>
  <div class="page-tag">5 OF 5</div>
  <div class="stage-head tone-green" style="left:20px;top:30px">
    <div class="st">STAGE 4</div><div class="sn">LEGACY &amp;<br>MULTIPLICATION</div><div class="rule"></div><div class="yrs">YEARS 31–40</div>
    <p class="lede" style="width:112px">Mentoring and multiplying leaders to leave a lasting Kingdom impact.</p>
  </div>
  <ul class="points" style="left:154px;top:34px">
    <li class="point" style="margin-bottom:11px"><span class="icon icon-ring-green"><svg width="16" height="16" viewBox="0 0 16 16"><circle cx="5" cy="6" r="2.5" fill="var(--green)"/><circle cx="11" cy="6" r="2.5" fill="var(--green)"/><path d="M1 14q4-6 7 0M8 14q4-6 7 0" fill="var(--green)"/></svg></span><div><h4 class="tone-green">Mentor Others</h4><p>Invest in and guide<br>the next generation</p></div></li>
    <li class="point" style="margin-bottom:11px"><span class="icon icon-ring-green"><svg width="16" height="16" viewBox="0 0 16 16"><path d="M3 3L13 13M13 3L3 13" stroke="var(--green)" stroke-width="1.3"/><g fill="var(--green)"><circle cx="3" cy="3" r="2"/><circle cx="13" cy="3" r="2"/><circle cx="3" cy="13" r="2"/><circle cx="13" cy="13" r="2"/><circle cx="8" cy="8" r="2"/></g></svg></span><div><h4 class="tone-green">Multiply Impact</h4><p>Empower others to<br>extend your reach</p></div></li>
    <li class="point" style="margin-bottom:11px"><span class="icon icon-ring-green"><svg width="16" height="16" viewBox="0 0 16 16"><circle cx="8" cy="8" r="6" fill="none" stroke="var(--green)" stroke-width="1.4"/><ellipse cx="8" cy="8" rx="2.5" ry="6" fill="none" stroke="var(--green)" stroke-width="1.2"/><path d="M2 8h12" stroke="var(--green)" stroke-width="1.2"/></svg></span><div><h4 class="tone-green">Leave a Legacy</h4><p>Create lasting Kingdom<br>fruit that endures</p></div></li>
    <li class="point"><span class="icon icon-ring-green"><svg width="16" height="14" viewBox="0 0 16 14"><path d="M1 3l4 4 3-5 3 5 4-4-2 8H3z" fill="var(--green)"/><rect x="3" y="12" width="10" height="1.5" fill="var(--green)"/></svg></span><div><h4 class="tone-green">Glorify God</h4><p>Finish well and<br>honor His call</p></div></li>
  </ul>
  <div class="brand" style="left:18px;top:314px"><span class="brand-dot" style="background:#fff"></span><span class="brand-name" style="font-size:18px;color:#fff">BLT</span></div>
  <div class="copyright" style="right:14px;top:322px;color:#fff">© 2026 BLT</div>
</section>

</body>
</html>
```